brochure for payroll services

we need a brochure design for our new payroll services- either to be send to prospect as an email attachment or print. see attached on content required.
our corporate colour is orange . the design should communicate trust ,and reliability with a breadth of fresh air.

```html
<!DOCTYPE html>
<html lang="en">
<head>
<meta charset="utf-8">
<title>Veridane Payroll Services Brochure</title>
<link rel="stylesheet" href="https://fonts.googleapis.com/css2?family=Open+Sans:wght@400;600;700;800&display=swap">
<style>
  :root {
    --paper-top: #ffffff;
    --paper-bottom: #f2f8fb;
    --ink: #2e2e2e;
    --ink-strong: #141414;
    --headline: #3a3a3a;
    --orange: #f7941d;
  }
  * { margin: 0; padding: 0; box-sizing: border-box; }
  html, body { width: 849px; height: 1200px; overflow: hidden; }
  body {
    position: relative;
    font-family: "Open Sans", Arial, sans-serif;
    color: var(--ink);
    background: linear-gradient(180deg, var(--paper-top), var(--paper-bottom));
  }
  .block { position: absolute; left: 227px; width: 560px; }
  .headline {
    top: 40px;
    font-weight: 700;
    font-size: 61px;
    line-height: 61px;
    letter-spacing: -1.2px;
    color: var(--headline);
  }
  .rule { position: absolute; height: 3px; background: var(--orange); }
  .rule--intro { left: 228px; top: 193px; width: 82px; }
  .rule--scope { left: 228px; top: 750px; width: 82px; }
  .rule--side { left: 19px; top: 750px; width: 43px; }
  .intro { top: 240px; font-size: 15.5px; line-height: 21.4px; }
  .intro strong { font-weight: 700; color: var(--ink-strong); }
  .section-title {
    font-weight: 800;
    font-size: 21.5px;
    line-height: 25px;
    color: var(--ink-strong);
  }
  .section-subtitle { font-weight: 700; font-size: 15px; line-height: 18px; color: var(--ink-strong); }
  .math { top: 324px; }
  .math p { margin-top: 20px; font-size: 15.5px; line-height: 21.4px; }
  .advantage { top: 516px; }
  .points { list-style: none; font-size: 15.5px; line-height: 21.3px; }
  .points li { position: relative; padding-left: 12px; }
  .points li::before { content: "»"; position: absolute; left: 0; top: 0; color: var(--orange); font-weight: 700; }
  .advantage-list { position: absolute; left: 215px; top: 585px; width: 560px; }
  .scope { top: 795px; }
  .scope-list { position: absolute; left: 215px; top: 841px; width: 560px; }
  .related-title { position: absolute; left: 228px; top: 1056px; font-weight: 600; font-size: 14.5px; color: var(--ink-strong); }
  .related-list { position: absolute; left: 215px; top: 1077px; width: 560px; }
  .brand { position: absolute; left: 19px; top: 826px; display: flex; align-items: center; gap: 8px; }
  .brand-mark { width: 26px; height: 26px; background: var(--orange); }
  .brand-name { font-weight: 700; font-size: 22px; color: var(--ink-strong); }
  .contact { position: absolute; left: 19px; top: 907px; font-size: 12px; line-height: 21.2px; font-weight: 600; color: var(--ink-strong); }
  .contact address { font-style: normal; }
  .contact .web { margin-top: 21px; font-weight: 700; }
  .contact .cta { margin-top: 21px; font-weight: 400; }
</style>
</head>
<body>
  <h1 class="block headline">WE PROCESS<br>YOUR PROCESS</h1>
  <div class="rule rule--intro"></div>

  <p class="block intro">We provide your company with <strong>payroll services</strong> and<br>offer you the peace of mind to focus on your core activities.</p>

  <section class="block math">
    <h2 class="section-title">LEAVE THE MATH TO US</h2>
    <p>We make sure that will not be distracted by technology selection,<br>implementation and maintenance, attracting and retaining expertise<br>and dedicated resources, keeping track of changes in regulations<br>and potential conflict of interests within (knowing the salary and<br>benefits for all).</p>
  </section>

  <section class="block advantage">
    <h2 class="section-title">TRUST, RELIABILITY AND EFFICIENCY</h2>
    <p class="section-subtitle">ADVANTAGE VERIDANE</p>
  </section>
  <ul class="points advantage-list">
    <li>Project management and methodology to ensure seamless transition<br>and sustainable delivery.</li>
    <li>Domain knowledge in payroll, accounting &amp; finance and taxes.</li>
    <li>Robust technology platform for automation, control and visibility.</li>
    <li>Proven delivery expertise and experience to provide reliable and<br>trusted services.</li>
  </ul>

  <div class="rule rule--side"></div>
  <div class="rule rule--scope"></div>

  <div class="brand">
    <span class="brand-mark"></span>
    <span class="brand-name">Veridane</span>
  </div>
  <div class="contact">
    <address>Veridane Private Limited<br>45 Harbour View Road<br>#05-12, Tidewater Hub<br>Singapore - 418802</address>
    <p class="web">contact@veridane.biz<br>www.veridane.biz</p>
    <p class="cta">Contact us to find out<br>how we can help you<br>and your business.</p>
  </div>

  <section class="block scope">
    <h2 class="section-title">SCOPE OF SERVICES</h2>
  </section>
  <ul class="points scope-list">
    <li>Process payroll (salary calculations) on monthly to bi-monthly basis</li>
    <li>Process gross to net salary and applicable CPF, CDAC, MBMF, SINDA<br>or ECF contributions</li>
    <li>Process bonuses, and any adhoc payments</li>
    <li>Process no-pay leave</li>
    <li>Salary disbursement to employees via Bank GIRO transfer</li>
    <li>Provide payroll report for management's review</li>
    <li>Prepare and submit CPF e-submission</li>
    <li>Prepare and submit year-end tax forms (Form IR8A)</li>
  </ul>

  <h3 class="related-title">OTHER RELATED SERVICES</h3>
  <ul class="points related-list">
    <li>Employee’s leave administration and management</li>
    <li>Timesheet management</li>
    <li>Claim management</li>
  </ul>
</body>
</html>
```